New Business Card

Would like a shiny card with Metallic logo raised on th front. Address 518 Whitlock Avenue, Toronto Ontario M4K2J8, phone 416 555 0182, email kvbe@lindenmail.ca and web www.kvbe.ca on the back in right and left lower corners balanced. Top of back should say Personalized Care for Pet's and their People centered. Leaving space on the back to write. Horizontal placement

Industry/Entity Type

Business

```html
<!DOCTYPE html>
<html lang="en">
<head>
<meta charset="utf-8">
<title>Kestrel Vale Animal Hospital – Business Card</title>
<link rel="stylesheet" href="https://fonts.googleapis.com/css2?family=Michroma&family=Roboto:wght@400&display=swap">
<style>
  :root {
    --backdrop: #3b3b3d;
    --card-black: #141414;
    --card-white: #ffffff;
    --silver: #c9c9cc;
    --swoop-grey: #8e8e8e;
    --swoop-light: #bdbdbd;
    --ink: #1a1a1a;
    --rule: #9a9a9a;
  }
  html, body {
    margin: 0;
    padding: 0;
    width: 799px;
    height: 1200px;
    overflow: hidden;
    background: var(--backdrop);
  }
  .canvas {
    position: relative;
    width: 799px;
    height: 1200px;
  }
  .card {
    position: absolute;
    left: 80px;
    width: 640px;
    height: 366px;
    border-radius: 4px;
    overflow: hidden;
    box-shadow: 0 10px 28px rgba(0,0,0,.45);
  }
  .card-front {
    top: 150px;
    background: var(--card-black);
    display: flex;
    align-items: center;
    justify-content: center;
  }
  .brand {
    display: flex;
    align-items: center;
    gap: 14px;
    font-family: "Michroma", sans-serif;
    color: var(--silver);
    font-size: 22px;
    letter-spacing: 1px;
    text-transform: uppercase;
  }
  .brand-dot {
    width: 22px;
    height: 22px;
    border-radius: 50%;
    background: var(--silver);
    flex: none;
  }
  .card-back {
    top: 690px;
    background: var(--card-white);
  }
  .back-art {
    position: absolute;
    inset: 0;
  }
  .contact {
    position: absolute;
    left: 30px;
    top: 54px;
    margin: 0;
    padding: 0;
    list-style: none;
    font-family: "Roboto", sans-serif;
    font-size: 14px;
    color: var(--ink);
    line-height: 19px;
  }
  .contact li {
    display: flex;
    align-items: center;
    gap: 12px;
  }
  .contact svg { width: 11px; height: 11px; fill: #555; flex: none; }
  .address {
    position: absolute;
    right: 24px;
    top: 88px;
    margin: 0;
    font-style: normal;
    font-family: "Roboto", sans-serif;
    font-size: 14px;
    line-height: 20px;
    color: var(--card-white);
    text-align: right;
  }
  .tagline {
    position: absolute;
    left: 30px;
    top: 200px;
    margin: 0;
    font-family: "Michroma", sans-serif;
    font-size: 15.5px;
    color: var(--ink);
    white-space: nowrap;
  }
  .write-lines {
    position: absolute;
    left: 30px;
    right: 30px;
    top: 222px;
  }
  .write-lines span {
    display: block;
    height: 40px;
    border-bottom: 1px solid var(--rule);
  }
</style>
</head>
<body>
<main class="canvas">
  <section class="card card-front" aria-label="Card front">
    <div class="brand">
      <span class="brand-dot"></span>
      <span class="brand-name">Kestrel Vale Animal Hospital</span>
    </div>
  </section>

  <section class="card card-back" aria-label="Card back">
    <svg class="back-art" viewBox="0 0 640 366" preserveAspectRatio="none" aria-hidden="true">
      <path d="M0 0 H640 V170 C530 165 430 130 360 90 C300 50 230 14 0 14 Z" fill="var(--card-black)"/>
      <path d="M0 24 C230 24 300 60 360 100 C430 140 530 175 640 180" fill="none" stroke="var(--swoop-grey)" stroke-width="8"/>
      <path d="M0 36 C230 36 300 72 360 112 C430 152 530 187 640 192" fill="none" stroke="var(--swoop-light)" stroke-width="5"/>
    </svg>

    <ul class="contact">
      <li><svg viewBox="0 0 12 12"><path d="M2 1h2l1 3-1.5 1a7 7 0 0 0 3.5 3.5L8 7l3 1v2a1 1 0 0 1-1 1A9 9 0 0 1 1 2a1 1 0 0 1 1-1z"/></svg>416 555 0182</li>
      <li><svg viewBox="0 0 12 12"><path d="M1 2h10v8H1z M1 2l5 4 5-4" fill="none" stroke="#555" stroke-width="1.4"/></svg>www.kvbe.ca</li>
      <li><svg viewBox="0 0 12 12"><circle cx="6" cy="6" r="5" fill="none" stroke="#555" stroke-width="1.2"/><path d="M1 6h10M6 1v10" stroke="#555" stroke-width="1"/></svg>kvbe@lindenmail.ca</li>
    </ul>

    <address class="address">518 Whitlock Avenue, Toronto<br>Ontario M4K2J8</address>

    <p class="tagline">Personalized Care for Pet's and their People</p>

    <div class="write-lines" aria-hidden="true">
      <span></span><span></span><span></span>
    </div>
  </section>
</main>
</body>
</html>
```